Business needs Office Posters Designed

I need a office poster designed to put on a 2 feet x 3 feet space:
My Employee is Better Than Me.
- to signify the importance of listening to your employees, because they know better, more experienced in their respective fields.

Target Market(s)

employees

Industry/Entity Type

Healthcare

```html
<!DOCTYPE html>
<html lang="en">
<head>
<meta charset="UTF-8">
<title>My Employee Is Better Than Me — Office Poster</title>
<link rel="stylesheet" href="https://fonts.googleapis.com/css2?family=Bebas+Neue&display=swap">
<style>
  :root {
    --canvas-bg: #ffffff;
    --poster-base: #1e6fc2;
    --poster-glow: #a9f1f4;
    --poster-mid: #2a8fd0;
    --poster-deep: #212f7c;
    --headline-white: #ffffff;
    --headline-accent: #00c6ff;
    --rule-light: #bff2ff;
  }
  html, body {
    margin: 0;
    padding: 0;
    width: 1200px;
    height: 1000px;
    overflow: hidden;
    background: var(--canvas-bg);
  }
  .stage {
    position: relative;
    width: 1200px;
    height: 1000px;
  }
  .poster {
    position: absolute;
    left: 464px;
    top: 296px;
    width: 272px;
    height: 407px;
    display: block;
  }
  .headline {
    font-family: "Bebas Neue", "Oswald", sans-serif;
  }
  .headline-white { fill: var(--headline-white); }
  .headline-accent { fill: var(--headline-accent); }
  .accent-frame {
    fill: none;
    stroke: var(--rule-light);
    stroke-width: 1;
    opacity: 0.75;
  }
</style>
</head>
<body>
<main class="stage">
  <svg class="poster" viewBox="0 0 272 407" xmlns="http://www.w3.org/2000/svg" role="img" aria-label="Poster: My Employee Is Better Than Me">
    <defs>
      <radialGradient id="poster-top-glow" cx="136" cy="0" r="190" gradientUnits="userSpaceOnUse">
        <stop offset="0" stop-color="var(--poster-glow)"/>
        <stop offset="0.45" stop-color="var(--poster-mid)" stop-opacity="0.85"/>
        <stop offset="1" stop-color="var(--poster-base)" stop-opacity="0"/>
      </radialGradient>
      <radialGradient id="poster-bottom-shade" cx="136" cy="407" r="150" gradientUnits="userSpaceOnUse">
        <stop offset="0" stop-color="var(--poster-deep)"/>
        <stop offset="0.6" stop-color="var(--poster-deep)" stop-opacity="0.45"/>
        <stop offset="1" stop-color="var(--poster-deep)" stop-opacity="0"/>
      </radialGradient>
      <linearGradient id="poster-side-light" x1="0" y1="0" x2="1" y2="0">
        <stop offset="0" stop-color="var(--poster-mid)" stop-opacity="0.6"/>
        <stop offset="0.25" stop-color="var(--poster-mid)" stop-opacity="0"/>
        <stop offset="0.75" stop-color="var(--poster-mid)" stop-opacity="0"/>
        <stop offset="1" stop-color="var(--poster-mid)" stop-opacity="0.6"/>
      </linearGradient>
      <linearGradient id="rule-fade" x1="0" y1="0" x2="1" y2="0">
        <stop offset="0" stop-color="var(--rule-light)" stop-opacity="0"/>
        <stop offset="0.5" stop-color="var(--rule-light)" stop-opacity="1"/>
        <stop offset="1" stop-color="var(--rule-light)" stop-opacity="0"/>
      </linearGradient>
    </defs>

    <rect class="poster-base" width="272" height="407" fill="var(--poster-base)"/>
    <rect class="poster-side-light" width="272" height="407" fill="url(#poster-side-light)"/>
    <rect class="poster-top-glow" width="272" height="407" fill="url(#poster-top-glow)"/>
    <rect class="poster-bottom-shade" width="272" height="407" fill="url(#poster-bottom-shade)"/>

    <rect class="rule rule-top" x="36" y="109.5" width="200" height="1.2" fill="url(#rule-fade)"/>
    <rect class="rule rule-bottom" x="36" y="297.5" width="200" height="1.2" fill="url(#rule-fade)"/>

    <g class="headline">
      <text class="headline-white" x="26" y="159" font-size="53" textLength="220" lengthAdjust="spacingAndGlyphs">MY EMPLOYEE</text>
      <text class="headline-white" x="26" y="221" font-size="77" textLength="40" lengthAdjust="spacingAndGlyphs">IS</text>
      <rect class="accent-frame" x="75.5" y="164.5" width="176" height="61"/>
      <text class="headline-accent" x="81" y="221" font-size="77" textLength="164" lengthAdjust="spacingAndGlyphs">BETTER</text>
      <text class="headline-white" x="26" y="287" font-size="76" textLength="220" lengthAdjust="spacingAndGlyphs">THAN ME</text>
    </g>
  </svg>
</main>
</body>
</html>
```